Guitar parts retail packaging

I have 2 boxes I need designed. This will be for my guitar parts. They are going to be thick cardstock type paper box, with a foam insert to secure the items. Matte finish with silver foil printing is sort of where im headed, but Im open to other beautiful design. The boxes will need to have a window on top of the box to show the product inside. Color scheme Im thinking with is Black with red, white and Silver foil printing. Unless you come up with something nicer, im open to that. But my business cards and some stickers are those colors.
2 different size boxes, but they can be the same basic design, modified for 2 different sizes. They will open at the front, and the lid will lift, hinged at the top back edge. (Please see purple box in picture for example for how box will work). Both boxes will have a window on top to showcase product in the box. One of the sides, (2" X 1.25") will be left a solid color, grey or other so I can put a product sticker on that side to designate what type of product is in the box. So you are really just designing the top (With window), front, back, and 1 side. Maybe something clever on the bottom but if thats blank thats fine.
LARGE BOX:
5.25 wide (Left to right)
2” deep (Front to back)
1.25” tall (Top to bottom)
SMALL BOX:
2” Wide (Left to right)
2” Deep (Front to back)
Please see Business card and sticker in picture for color scheme Im thinking. ( I am open to other colors and designs as well)

Target Market(s)

Musicians, Rockers, tattoo junkies, general badasses.

Industry/Entity Type

Guitar industry. Rock & Rollers

Font styles to use
Other font styles liked:
• I use a font called Morpheus for my logo. Also Times New Roman, maybe Copperplate? Or something more creative? Im open as long as it fits.

Colors
EB3D1F
EC4F4E
F09395
F8D3D4
FCEDEE

Requirements
Must have
• My Company name and logo (Harrow Kestrel). Also slogan-
Nice to have
• Please see general aesthetic in sticker and biz card.
Should not have
• No horror themes, keep it cool and classy. (Even though logo is a skull). And please no pictures of guitars on the box. You might add a pic of 1 type of guitar, but the parts inside might not fit that guitar pictured on the box.

```html
<!DOCTYPE html>
<html lang="en">
<head>
<meta charset="utf-8">
<title>Harrow Kestrel – Guitar Parts Box</title>
<link rel="stylesheet" href="https://fonts.googleapis.com/css2?family=Cinzel:wght@400;600&display=swap">
<style>
  :root {
    --backdrop: #d2d2d2;
    --lid-black: #0d0d0d;
    --lid-black-soft: #1c1c1c;
    --crimson-deep: #7d0a0e;
    --crimson: #b3141a;
    --silver: #bdbdbd;
    --silver-light: #d9d9d9;
    --window: #ececec;
    --foil: #e8e8e8;
    --text-font: "Cinzel", serif;
  }
  * { margin: 0; padding: 0; box-sizing: border-box; }
  html, body {
    width: 1200px;
    height: 882px;
    overflow: hidden;
    background: var(--backdrop);
  }
  .box-net {
    position: absolute;
    left: 100px;
    top: 150px;
    width: 1000px;
  }
  .lid-panel {
    position: relative;
    height: 170px;
    background: linear-gradient(90deg, var(--lid-black) 0%, var(--lid-black-soft) 50%, var(--lid-black) 100%);
  }
  .lid-brand {
    position: absolute;
    left: 490px;
    top: 52px;
    width: 460px;
    text-align: center;
    color: var(--foil);
    font-family: var(--text-font);
    white-space: nowrap;
  }
  .lid-brand .brand-name {
    font-size: 38px;
    font-weight: 600;
    letter-spacing: 1px;
    line-height: 1;
  }
  .lid-brand .slogan {
    margin-top: 10px;
    font-size: 17px;
    letter-spacing: 2px;
  }
  .front-panel {
    position: relative;
    height: 420px;
  }
  .front-panel svg { display: block; }
  .front-brand {
    position: absolute;
    left: 15px;
    top: 140px;
    width: 305px;
    text-align: center;
    color: var(--foil);
    font-family: var(--text-font);
    white-space: nowrap;
  }
  .front-brand .brand-mark {
    display: block;
    width: 22px;
    height: 22px;
    margin: 0 auto 14px;
    border-radius: 50%;
    background: var(--foil);
  }
  .front-brand .brand-name {
    font-size: 30px;
    font-weight: 600;
    line-height: 1;
  }
  .front-brand .slogan {
    margin-top: 10px;
    font-size: 14px;
    letter-spacing: 1.5px;
  }
</style>
</head>
<body>
  <div class="box-net">
    <section class="lid-panel" role="img" aria-label="Black lid panel with tonal damask ornament pattern">
      <div class="lid-brand">
        <div class="brand-name">Harrow Kestrel</div>
        <div class="slogan">Loud &amp; Proud Legacy</div>
      </div>
    </section>

    <section class="front-panel">
      <svg width="1000" height="420" viewBox="0 0 1000 420">
        <defs>
          <linearGradient id="crimson-fade" x1="0" y1="0" x2="1" y2="1">
            <stop offset="0" stop-color="#7d0a0e"/>
            <stop offset="0.5" stop-color="#b3141a"/>
            <stop offset="1" stop-color="#7d0a0e"/>
          </linearGradient>
          <linearGradient id="silver-fade" x1="0" y1="0" x2="1" y2="1">
            <stop offset="0" stop-color="#d9d9d9"/>
            <stop offset="1" stop-color="#bdbdbd"/>
          </linearGradient>
        </defs>
        <rect class="silver-field" x="0" y="0" width="1000" height="420" fill="url(#silver-fade)"
              role="img" aria-label="Silver filigree ornament pattern"/>
        <polygon class="crimson-field" points="0,0 720,0 420,420 0,420" fill="url(#crimson-fade)"
                 role="img" aria-label="Crimson damask ornament pattern"/>
        <path class="thumb-notch" d="M535 0 A30 30 0 0 0 595 0 Z" fill="#0d0d0d"/>
        <rect class="product-window" x="330" y="30" width="640" height="360" rx="42" fill="#ececec"/>
      </svg>
      <div class="front-brand">
        <span class="brand-mark"></span>
        <div class="brand-name">Harrow Kestrel</div>
        <div class="slogan">Loud &amp; Proud Legacy</div>
      </div>
    </section>
  </div>
</body>
</html>
```